Amber Heron Fund Pitch Deck

This is a PowerPoint for use in investor presentations. The copy is written (although it may have small tweaks) and the designer will be responsible for creating a template and some graphical representations inside the presentation.

Note on the logo. Only the Amber Heron should be used, not the text.

```html
<!DOCTYPE html>
<html lang="en">
<head>
<meta charset="utf-8">
<title>Amber Heron Fund – Pitch Deck</title>
<link href="https://fonts.googleapis.com/css2?family=Ubuntu:wght@300;400;500;700&display=swap" rel="stylesheet">
<style>
:root{
  --blue:#5d7ec4;
  --blue-light:#8aa3d8;
  --blue-pale:#c9d5ee;
  --blue-dark:#2f4f94;
  --ink:#3d3d3d;
  --grey:#6b6b6b;
  --dark-box:#4a4a4a;
  --sheet:#dedede;
  --white:#ffffff;
}
*{box-sizing:border-box;margin:0;padding:0}
html,body{width:1200px;height:3098px;overflow:hidden}
body{background:var(--sheet);font-family:"Ubuntu",sans-serif;color:var(--ink);position:relative}
.hero{position:absolute;left:0;top:0;width:1200px;height:800px;background:linear-gradient(180deg,#f4f4f4 0%,#e2e2e2 60%,#cdcdcd 100%)}
.hero-brand{position:absolute;left:62px;top:64px;display:flex;align-items:center;gap:8px;color:var(--blue);font-size:22px;font-weight:500}
.dot{display:inline-block;width:10px;height:10px;border-radius:50%;background:currentColor}
.hero-frame{position:absolute;left:260px;top:160px;width:540px;height:303px;transform:scale(1.26);transform-origin:0 0;box-shadow:0 20px 50px rgba(0,0,0,.25)}
.slide{position:absolute;width:540px;height:303px;background:var(--white);overflow:hidden}
.photo{position:absolute}
.brand{position:absolute;display:flex;align-items:center;gap:5px;font-weight:500;color:var(--blue)}
.footer-brand{left:12px;bottom:10px;font-size:10px}
.page{position:absolute;right:12px;bottom:12px;font-size:5px;color:var(--grey);letter-spacing:.5px}
.cover-title{position:absolute;left:36px;top:118px;font-size:28px;font-weight:300;line-height:30px;color:var(--blue)}
.cover-text{position:absolute;left:36px;top:186px;width:245px;font-size:7px;line-height:8px}
.badge{position:absolute;left:36px;top:237px;background:var(--blue);color:#fff;font-size:5.5px;padding:4px 12px}
.copy{position:absolute;right:26px;bottom:22px;font-size:5px;color:#fff}
.cover-alt{background:var(--blue)}
.cover-alt .cover-title,.cover-alt .cover-text{color:#fff}
.cover-alt .badge{background:#fff;color:var(--blue)}
.slide-title{position:absolute;width:100%;text-align:center;font-size:17px;font-weight:300;color:var(--blue)}
.slide-title b{font-weight:700}
.small{font-size:5.5px;line-height:6.5px}
.body{font-size:9.5px;line-height:11px}
ul.bio{list-style:disc;padding-left:8px;font-size:5px;line-height:6px;color:var(--ink)}
.namebar{background:var(--blue-light);color:#fff;padding:3px 8px;font-size:11px}
.namebar b{font-weight:700}
.namebar span{display:block;font-size:5px}
.pt{position:absolute;font-size:7px;line-height:8px;text-align:center;color:var(--ink)}
.icon{position:absolute;width:26px;height:26px;border-radius:50%;background:var(--blue);color:#fff;font-size:11px;font-weight:700;display:flex;align-items:center;justify-content:center}
.stat-box{position:absolute;background:var(--blue);color:#fff;text-align:center}
.pct{position:absolute;width:160px;text-align:center}
.pct .num{font-size:22px;font-weight:300;color:var(--grey)}
.pct .lab{font-size:9px;color:var(--blue)}
.pct .txt{font-size:5.5px;line-height:6.5px;color:var(--grey)}
.mgmt{position:absolute;top:92px;width:145px}
.mgmt h4{font-size:10px;color:var(--blue);font-weight:400}
.mgmt h4 b{font-weight:700}
.mgmt .role{font-size:5px;margin-bottom:10px}
</style>
</head>
<body>

<section class="hero">
  <div class="hero-brand"><span class="dot"></span>Amber Heron</div>
  <div class="hero-frame">
    <div class="slide" style="left:0;top:0">
      <div class="photo" role="img" aria-label="Photo of a businessman signing documents with charts on the desk" style="right:0;top:0;width:340px;height:303px;background:linear-gradient(135deg,#e9edf3,#7f8797 60%,#2f3440)"></div>
      <svg style="position:absolute;left:0;top:0" width="540" height="303"><polygon points="0,0 260,0 200,303 0,303" fill="#fff"/><polygon points="260,0 330,0 240,220" fill="#fff" opacity=".7"/><polygon points="230,303 540,120 540,303" fill="#5d7ec4"/><polygon points="300,303 540,200 540,303" fill="#2f4f94" opacity=".5"/></svg>
      <div class="brand" style="left:36px;top:40px;font-size:11px"><span class="dot"></span>Amber Heron</div>
      <div class="cover-title">Amber Heron<br>NPL Fund</div>
      <div class="cover-text">Experience with fund management and asset disposal. Utilizing the clues and hints that borrowers and guarantors leave on the Internet, we can special service assets and collect on them more quickly and maximize return.</div>
      <div class="badge">Wednesday, October 26, 2022</div>
      <div class="copy">Copyright © 2022 Amber Heron</div>
    </div>
  </div>
</section>

<!-- Slide 1 : cover light -->
<div class="slide" style="left:51px;top:812px">
  <div class="photo" role="img" aria-label="Photo of a businessman signing documents with charts on the desk" style="right:0;top:0;width:340px;height:303px;background:linear-gradient(135deg,#e9edf3,#7f8797 60%,#2f3440)"></div>
  <svg style="position:absolute;left:0;top:0" width="540" height="303"><polygon points="0,0 260,0 200,303 0,303" fill="#fff"/><polygon points="260,0 330,0 240,220" fill="#fff" opacity=".7"/><polygon points="230,303 540,120 540,303" fill="#5d7ec4"/><polygon points="300,303 540,200 540,303" fill="#2f4f94" opacity=".5"/></svg>
  <div class="brand" style="left:36px;top:40px;font-size:11px"><span class="dot"></span>Amber Heron</div>
  <div class="cover-title">Amber Heron<br>NPL Fund</div>
  <div class="cover-text">Experience with fund management and asset disposal. Utilizing the clues and hints that borrowers and guarantors leave on the Internet, we can special service assets and collect on them more quickly and maximize return.</div>
  <div class="badge">Wednesday, October 26, 2022</div>
  <div class="copy">Copyright © 2022 Amber Heron</div>
</div>

<!-- Slide 2 : cover blue -->
<div class="slide cover-alt" style="left:609px;top:812px">
  <div class="photo" role="img" aria-label="Photo of a businessman reviewing printed charts" style="right:0;top:0;width:300px;height:303px;background:linear-gradient(135deg,#dfe4ec,#8a93a6 60%,#39404f)"></div>
  <svg style="position:absolute;left:0;top:0" width="540" height="303"><polygon points="0,0 250,0 190,303 0,303" fill="#5d7ec4"/><polygon points="220,303 540,160 540,303" fill="#5d7ec4" opacity=".85"/><polygon points="250,0 300,0 230,150" fill="#5d7ec4" opacity=".6"/></svg>
  <div class="brand" style="left:36px;top:40px;font-size:11px;color:#fff"><span class="dot"></span>Amber Heron</div>
  <div class="cover-title">Amber Heron<br>NPL Fund</div>
  <div class="cover-text">Experience with fund management and asset disposal. Utilizing the clues and hints that borrowers and guarantors leave on the Internet, we can special service assets and collect on them more quickly and maximize return.</div>
  <div class="badge">Wednesday, October 26, 2022</div>
  <div class="copy" style="color:var(--blue-pale)">Copyright © 2022 Amber Heron</div>
</div>

<!-- Slide 3 : The Edge -->
<div class="slide" style="left:51px;top:1133px">
  <div class="photo" role="img" aria-label="Photo of two business people shaking hands" style="left:300px;top:0;width:195px;height:256px;background:linear-gradient(135deg,#b9c3d4,#6c7587)"></div>
  <div style="position:absolute;left:0;top:170px;width:540px;height:86px;background:var(--blue);opacity:.92"></div>
  <div style="position:absolute;left:43px;top:40px;font-size:17px;font-weight:300;color:var(--blue)">The <b style="font-weight:700">EDGE</b></div>
  <div class="body" style="position:absolute;left:43px;top:78px;width:235px">Experience with fund management and asset disposal. Utilizing the clues and hints that borrowers and guarantors leave on the Internet, we can special service assets and collect on them more quickly and maximize return.</div>
  <div class="body" style="position:absolute;left:43px;top:185px;width:430px;color:#fff">Much of the technology and experience as a team can be attributed to the team's experience at Northfield. The principals were the management team that came on in March 2020 and grew the business from less than 12,000 PPP loans to more than 800,000.</div>
  <div class="brand footer-brand"><span class="dot"></span>Amber Heron</div><div class="page">PAGE | 3</div>
</div>

<!-- Slide 4 : Technology -->
<div class="slide" style="left:609px;top:1133px">
  <div class="slide-title" style="top:22px">The <b>TECHNOLOGY</b></div>
  <div class="photo" role="img" aria-label="Photo of a pen over printed bar charts" style="left:0;top:66px;width:540px;height:98px;background:linear-gradient(90deg,#eef0f4,#c7cdd8 50%,#e4d6cf)"></div>
  <div style="position:absolute;left:26px;top:183px;width:490px;font-size:9px;line-height:10.5px">
    <p style="margin-bottom:4px">Most lenders and servicers use <b>LedgerCore</b> or <b>ServiceLine</b> and then software like <b>CollectPro</b> for collections.</p>
    <p style="margin-bottom:4px">These software packages fail to address the most important factors which is to analyze the borrower (and the guarantors) to allow for customized collection plans. We use enhanced skip tracing developed during PPP forgiveness and collection efforts with advanced social media logic.</p>
    <p>Finally, we use evolving algorithms to price and purchase NPL portfolios at the correct price.</p>
  </div>
  <div class="brand footer-brand"><span class="dot"></span>Amber Heron</div><div class="page">PAGE | 4</div>
</div>

<!-- Slide 5 : People -->
<div class="slide" style="left:51px;top:1455px">
  <div class="photo" role="img" aria-label="Portrait photo of a team member in blue tint" style="left:33px;top:0;width:144px;height:158px;background:linear-gradient(180deg,#8aa3d8,#5d7ec4)"></div>
  <div style="position:absolute;left:33px;top:78px;width:144px;text-align:center;color:#fff;font-size:16px;line-height:18px;font-weight:300">The<br><b style="font-weight:700">PEOPLE</b></div>
  <div class="namebar" style="position:absolute;left:33px;top:165px;width:144px;background:var(--blue)"><b>Grant</b> Holloway<span>Managing Partner, Investment Committee</span></div>
  <ul class="bio" style="position:absolute;left:42px;top:198px;width:132px"><li>More than 20 years of banking experience with several national and regional banks</li><li>Director of a capital management firm, in less than 5 years achieved strong AUM and outsized returns managing distressed assets. Developed framework for additional funds.</li><li>CEO of Northfield.</li></ul>
  <div class="namebar" style="position:absolute;left:198px;top:33px;width:143px"><b>Daniel</b> Marsh<span>Managing Partner, Investment Committee</span></div>
  <ul class="bio" style="position:absolute;left:206px;top:66px;width:132px"><li>Founder of a law firm in Scottsdale, Arizona which became the first law firm in the country sold to private non-lawyer investors.</li><li>Extensive experience with large transactions including leading a large 2017 Arizona transaction on behalf of a client. Known for liquidation sales inside bankruptcy. Speaker at a national bankruptcy conference in Las Vegas.</li><li>COO of an early web development company that first implemented a commercially successful e-commerce campaign. Developer of associate software suite for non-profit management.</li><li>General Counsel of Northfield.</li></ul>
  <div class="namebar" style="position:absolute;left:198px;top:182px;width:143px"><b>Leo</b> Brandt<span>Chief Operating Officer</span></div>
  <ul class="bio" style="position:absolute;left:206px;top:216px;width:132px"><li>Management Consultant at two large advisory firms</li><li>Founder of two companies that grew to more than 1,000 employees.</li><li>COO of Northfield.</li></ul>
  <div class="namebar" style="position:absolute;left:363px;top:33px;width:143px"><b>Owen</b> Castell<span>Investment Committee</span></div>
  <ul class="bio" style="position:absolute;left:371px;top:66px;width:132px"><li>CEO of a listed impact corporation</li><li>CEO, regional bank</li><li>Director, community bank</li><li>Member, regional corporate directors association</li></ul>
  <div class="namebar" style="position:absolute;left:363px;top:130px;width:143px"><b>Peter</b> Lindqvist<span>Director of Credit Analytics</span></div>
  <ul class="bio" style="position:absolute;left:371px;top:163px;width:132px"><li>Product and data specialist with more than 15 years technology and startup experience.</li><li>Founded a communications firm which combined email and chat for customer success professionals. Raised capital and had more than 40,000 users.</li><li>Led advertising products at two media firms and grew revenue over 5 years.</li><li>Advisory board member of a venture capital firm.</li><li>VP, Products, Northfield.</li></ul>
  <div class="brand footer-brand"><span class="dot"></span>Amber Heron</div><div class="page">PAGE | 5</div>
</div>

<!-- Slide 6 : Market -->
<div class="slide" style="left:609px;top:1455px">
  <div style="position:absolute;left:180px;top:18px;width:340px;height:250px;background:var(--blue)"></div>
  <div class="photo" role="img" aria-label="Photo of hands reviewing financial charts on a desk" style="left:25px;top:26px;width:490px;height:60px;background:linear-gradient(90deg,#e6e9ef,#9aa2b1 50%,#545c6a)"></div>
  <div style="position:absolute;left:25px;top:106px;font-size:16px;line-height:17px;font-weight:300;color:var(--blue)">The<br><b style="font-weight:700">MARKET</b></div>
  <div style="position:absolute;left:25px;top:146px;width:145px;font-size:6.5px;line-height:7.5px">The commercial lending market size was valued at <b>$8,823.53</b> billion in <b>2020</b>, and is projected to reach <b>$29,379.83</b> billion by <b>2030</b>, growing at a CAGR of <b>13.1%</b> from <b>2021</b> to <b>2030</b>.</div>
  <div style="position:absolute;left:25px;top:197px;font-size:6.5px">Source:</div>
  <div style="position:absolute;left:25px;top:207px;width:145px;font-size:5px;color:var(--blue);text-decoration:underline">https://www.example-research.com/commercial-lending-market</div>
  <svg style="position:absolute;left:180px;top:118px" width="200" height="110" font-family="Ubuntu,sans-serif">
    <rect x="10" y="0" width="175" height="108" fill="#fff"/>
    <g font-size="4.5" fill="#555" text-anchor="end"><text x="22" y="8">35000</text><text x="22" y="20">30000</text><text x="22" y="32">25000</text><text x="22" y="44">20000</text><text x="22" y="56">15000</text><text x="22" y="68">10000</text><text x="22" y="80">5000</text><text x="22" y="92">0</text></g>
    <line x1="26" y1="90" x2="175" y2="90" stroke="#999" stroke-width=".5"/>
    <rect x="78" y="69" width="28" height="21" fill="#5d7ec4"/><rect x="115" y="20" width="28" height="70" fill="#2f4f94"/>
    <text x="92" y="67" font-size="4.5" text-anchor="middle" fill="#333">8823.53</text><text x="129" y="18" font-size="4.5" text-anchor="middle" fill="#333">29379.83</text>
    <text x="110" y="99" font-size="4.5" text-anchor="middle" fill="#555">YEAR</text>
  </svg>
  <div style="position:absolute;left:368px;top:153px;font-size:5px;color:#fff;line-height:8px">■ 2020<br>■ 2030</div>
  <div style="position:absolute;left:405px;top:148px;width:100px;font-size:7px;line-height:8px;color:#fff;text-align:center">The credit cycle is entering into a period of rising interest rates and corresponding defaults. The fund seeks to take advantage of that emerging opportunity.</div>
  <div class="brand footer-brand"><span class="dot"></span>Amber Heron</div><div class="page">PAGE | 6</div>
</div>

<!-- Slide 7 : Process -->
<div class="slide" style="left:51px;top:1777px">
  <div class="slide-title" style="top:22px">Our <b>PROCESS</b></div>
  <div style="position:absolute;left:0;top:132px;width:540px;height:14px;background:#ececec"></div>
  <div class="pt" style="left:20px;top:83px;width:90px">Work with our lender customers on their non-performing loan portfolio.</div>
  <div class="pt" style="left:120px;top:74px;width:80px">Provide special servicing in compliance with bank's servicing criteria.</div>
  <div class="pt" style="left:285px;top:83px;width:100px">Maintain first right of refusal to purchase loan using proprietary algorithm.</div>
  <div class="pt" style="left:410px;top:100px;width:100px">Liquidation, when necessary.</div>
  <div class="pt" style="left:85px;top:172px;width:90px">Purchase participation in non-performing loans.</div>
  <div class="pt" style="left:225px;top:172px;width:80px">Provide bank access to NPL platform.</div>
  <div class="pt" style="left:355px;top:172px;width:80px">Internal servicing standards.</div>
  <div class="icon" style="left:50px;top:145px">●</div>
  <div class="icon" style="left:117px;top:106px">$</div>
  <div class="icon" style="left:186px;top:145px">$</div>
  <div class="icon" style="left:254px;top:106px">⇄</div>
  <div class="icon" style="left:323px;top:145px">▦</div>
  <div class="icon" style="left:392px;top:106px">⚙</div>
  <div class="icon" style="left:460px;top:145px">✓</div>
  <div style="position:absolute;left:0;top:225px;width:540px;height:26px;background:var(--blue-light);color:#fff;font-size:7px;line-height:8px;text-align:center;padding-top:5px">Initially partner with licensed collection agencies to supplement our in-house abilities<br>(and comply with regulatory requirements). Potential to acquire and bring completely in-house.</div>
  <div class="brand footer-brand"><span class="dot"></span>Amber Heron</div><div class="page">PAGE | 7</div>
</div>

<!-- Slide 8 : Customers -->
<div class="slide" style="left:609px;top:1777px">
  <div class="slide-title" style="top:55px">Our <b>CUSTOMERS</b></div>
  <div style="position:absolute;left:12px;top:106px;width:246px;height:115px;background:var(--dark-box);color:#fff;font-size:9px;line-height:10px;padding:30px 14px 0">Target Market (It would seem we should narrow the target market and also point out any special relationships, people that Grant can source from last experience or otherwise explain why we have a leg up on pipeline.</div>
  <div class="stat-box" style="left:262px;top:106px;width:127px;height:115px">
    <div style="font-size:8px;line-height:9px;padding-top:10px">Community<br>Banks</div>
    <div style="position:absolute;left:0;top:37px;width:100%;height:78px;background:var(--blue-light)"><div style="font-size:24px;padding-top:18px">5,000</div><div style="font-size:6px">Nearly</div></div>
  </div>
  <div class="stat-box" style="left:393px;top:106px;width:127px;height:115px">
    <div style="font-size:8px;line-height:9px;padding-top:10px">Mid-market<br>Banks</div>
    <div style="position:absolute;left:0;top:37px;width:100%;height:78px;background:var(--blue-light)"><div style="font-size:24px;padding-top:18px">4,000</div><div style="font-size:6px">Approximately</div></div>
  </div>
  <div class="brand footer-brand"><span class="dot"></span>Amber Heron</div><div class="page">PAGE | 8</div>
</div>

<!-- Slide 9 : Advantage -->
<div class="slide" style="left:51px;top:2098px">
  <div class="slide-title" style="top:22px"><b>ADVANTAGE:</b> Tech + Capital</div>
  <div class="pct" style="left:14px;top:70px"><div class="num">25%</div><div class="lab">Lorem Ipsum Dolor</div><div class="txt">Nunc placerat, arcu nec mattis fermentum, nisi mauris convallis nunc, ut luctus nunc nisl id ex.</div></div>
  <div class="pct" style="left:14px;top:168px"><div class="num">12%</div><div class="lab">Lorem Ipsum Dolor</div><div class="txt">Nunc placerat, arcu nec mattis fermentum, nisi mauris convallis nunc, ut luctus nunc nisl id ex.</div></div>
  <div class="pct" style="left:363px;top:70px"><div class="num">20%</div><div class="lab">Lorem Ipsum Dolor</div><div class="txt">Nunc placerat, arcu nec mattis fermentum, nisi mauris convallis nunc, ut luctus nunc nisl id ex.</div></div>
  <div class="pct" style="left:363px;top:168px"><div class="num">36%</div><div class="lab">Lorem Ipsum Dolor</div><div class="txt">Nunc placerat, arcu nec mattis fermentum, nisi mauris convallis nunc, ut luctus nunc nisl id ex.</div></div>
  <div style="position:absolute;left:170px;top:112px;width:198px;height:102px;border-radius:50%;background:#24365f"></div>
  <div role="img" aria-label="Pie chart: 20%, 36%, 12%, 25%" style="position:absolute;left:170px;top:100px;width:198px;height:102px;border-radius:50%;background:conic-gradient(#5d7ec4 0 21.5%,#2f4f94 21.5% 60.2%,#3a3a3a 60.2% 73.1%,#7a7a7a 73.1% 100%)"></div>
  <div style="position:absolute;left:206px;top:116px;font-size:6px;color:#fff">25%</div>
  <div style="position:absolute;left:305px;top:112px;font-size:6px;color:#fff">20%</div>
  <div style="position:absolute;left:186px;top:152px;font-size:6px;color:#fff">12%</div>
  <div style="position:absolute;left:312px;top:166px;font-size:6px;color:#fff">36%</div>
  <div class="brand footer-brand"><span class="dot"></span>Amber Heron</div><div class="page">PAGE | 9</div>
</div>

<!-- Slide 10 : Management -->
<div class="slide" style="left:609px;top:2098px">
  <div class="slide-title" style="top:22px">MANAGEMENT Structure</div>
  <div style="position:absolute;top:52px;width:100%;text-align:center;font-size:7px">Investment Committee</div>
  <div style="position:absolute;left:190px;top:92px;width:1px;height:150px;background:#ccc"></div>
  <div style="position:absolute;left:355px;top:92px;width:1px;height:150px;background:#ccc"></div>
  <div class="mgmt" style="left:42px"><h4><b>Owen</b> Castell</h4><div class="role">Investment Committee</div><ul class="bio"><li>CEO of a listed impact corporation</li><li>CEO, regional bank</li><li>Director, community bank</li><li>Member, regional corporate directors association</li></ul></div>
  <div class="mgmt" style="left:207px"><h4><b>Grant</b> Holloway</h4><div class="role">Managing Partner, Investment Committee</div><ul class="bio"><li>More than 20 years of banking experience with several national and regional banks</li><li>Director of a capital management firm, in less than 5 years achieved strong AUM and outsized returns managing distressed assets. Developed framework for additional funds.</li><li>CEO of Northfield.</li></ul></div>
  <div class="mgmt" style="left:372px"><h4><b>Daniel</b> Marsh</h4><div class="role">Managing Partner, Investment Committee</div><ul class="bio"><li>Founder of a law firm in Scottsdale, Arizona which became the first law firm in the country sold to private non-lawyer investors.</li><li>Extensive experience with large transactions including a large 2017 Arizona transaction on behalf of a client. Known for liquidation sales inside bankruptcy.</li><li>COO of an early web development company that first implemented a commercially successful e-commerce campaign.</li><li>General Counsel of Northfield.</li></ul></div>
  <div class="brand footer-brand"><span class="dot"></span>Amber Heron</div><div class="page">PAGE | 10</div>
</div>

<!-- Slide 11 : Co-Sponsored Fund -->
<div class="slide" style="left:51px;top:2420px">
  <div class="photo" role="img" aria-label="Photo of colleagues reviewing charts at a table" style="left:280px;top:0;width:220px;height:265px;background:linear-gradient(135deg,#d9c7b2,#c9ccd3 50%,#9aa4b6)"></div>
  <div style="position:absolute;left:38px;top:62px;font-size:16px;line-height:18px;color:var(--blue)"><b>WAYPOINT</b><br><span style="font-weight:300">Co-Sponsored Fund</span></div>
  <ul style="position:absolute;left:38px;top:125px;width:210px;font-size:9px;line-height:10px;list-style:square;padding-left:8px">
    <li style="margin-bottom:8px">Utilize Waypoint network, AMHR technology</li>
    <li>Joint LP Investment, Waypoint affiliates / partners to provide additional LP Investment <b>NPLHeron</b>, LLC to be GP, <b>80%</b> of carry to AMHR and <b>20%</b> to Waypoint</li>
  </ul>
  <div class="brand footer-brand"><span class="dot"></span>Amber Heron</div><div class="page">PAGE | 11</div>
</div>

<!-- Slide 12 : Projected size -->
<div class="slide" style="left:609px;top:2420px">
  <div style="position:absolute;left:30px;top:110px;width:200px;text-align:center;font-size:16px;line-height:18px;color:var(--blue)"><b>PROJECTED</b><br><span style="font-weight:300">Size of Fund</span></div>
  <div style="position:absolute;left:30px;top:165px;width:200px;text-align:center;font-size:15px;line-height:17px">Initially <b>$200</b> million,<br>up to <b>$1</b> billion</div>
  <div style="position:absolute;left:276px;top:80px;width:225px;height:142px;background:var(--blue-light)"></div>
  <div style="position:absolute;left:276px;top:80px;width:225px;height:42px;background:var(--blue);color:#fff;text-align:center;font-size:22px;font-weight:700;padding-top:8px">$100</div>
  <div style="position:absolute;left:388px;top:130px;width:1px;height:85px;background:var(--blue-pale)"></div>
  <div style="position:absolute;left:283px;top:147px;width:100px;color:#fff;text-align:center;font-size:9px;line-height:10px">million commitment from AMHR from funds due from CPF</div>
  <div style="position:absolute;left:394px;top:147px;width:100px;color:#fff;text-align:center;font-size:9px;line-height:10px">million commitment from Waypoint or its affiliates</div>
  <div class="brand footer-brand"><span class="dot"></span>Amber Heron</div><div class="page">PAGE | 12</div>
</div>

<!-- Slide 13 : Contact -->
<div class="slide" style="left:331px;top:2742px;background:var(--blue)">
  <div class="photo" role="img" aria-label="Faint photo of a business meeting under blue tint" style="left:0;top:0;width:540px;height:303px;background:linear-gradient(135deg,#6f8dcc,#5d7ec4 50%,#5473b8);opacity:.9"></div>
  <div class="brand" style="left:0;top:105px;width:540px;justify-content:center;font-size:16px;color:#fff"><span class="dot"></span>Amber Heron</div>
  <div style="position:absolute;top:178px;width:100%;text-align:center;font-size:13px;color:#fff;font-weight:300">Contact Us</div>
  <div style="position:absolute;top:213px;width:100%;display:flex;justify-content:center;gap:18px;font-size:7px;color:#fff">
    <span>☏ Phone Number Goes Here</span><span>✉ E-Mail Address Goes Here</span><span>◎ URL Address Goes Here</span>
  </div>
</div>

</body>
</html>
```